Commercial construction contractor website.

We need a website that contains About Us, Contact info, Services, Project pictures and Industry News section

Target Market(s)

I'm building industral/flex spaces/commercial.

Industry/Entity Type

Commercial/industrial construction

Coding

Coded - Design and coding required

Number of Pages Required

5+ page

Font styles to use
Other font styles liked:
• The logo font is Microgramma Pro

Requirements
Must have
• Must have correct company name spelling: Dunmore Ridge Construction
Nice to have
• I do like to see our logo design implemented in the design
Should not have
• Please do not show big city pictures and business suit people. We are a commercial construction company

```html
<!DOCTYPE html>
<html lang="en">
<head>
<meta charset="utf-8">
<title>Dunmore Ridge Construction</title>
<link rel="stylesheet" href="https://fonts.googleapis.com/css2?family=Archivo:wght@500;600;700;800&family=Arimo:wght@400;500&family=Montserrat:wght@400;500;600;700&display=swap">
<style>
:root{
  --blue:#0b3a94;
  --blue-deep:#082a72;
  --blue-bright:#1663c4;
  --ink:#111111;
  --body:#3d3d3d;
  --band:#f3f5f8;
  --white:#ffffff;
  --footer:#141414;
  --copy-font:"Arimo",sans-serif;
}
*{margin:0;padding:0;box-sizing:border-box}
html,body{width:1200px;height:4688px;overflow:hidden;background:var(--white)}
body{font-family:"Montserrat",sans-serif;color:var(--ink);position:relative}

/* header */
.site-header{position:absolute;left:0;top:0;width:1200px;height:98px;background:var(--white)}
.brand{position:absolute;left:113px;top:22px;display:flex;align-items:center;gap:10px}
.brand-mark{width:34px;height:34px;background:var(--blue)}
.brand-name{font-family:"Montserrat",sans-serif;font-weight:700;font-size:13px;line-height:16px;color:var(--blue);letter-spacing:.5px;width:150px}
.contact-bar{position:absolute;right:110px;top:17px;display:flex;gap:22px;font-size:17px;font-weight:500;color:var(--ink)}
.contact-item{display:flex;align-items:center;gap:10px}
.contact-icon{width:32px;height:32px;border-radius:50%;background:var(--blue);display:flex;align-items:center;justify-content:center}
.main-nav{position:absolute;right:110px;top:64px;display:flex;gap:52px;font-size:17px;font-weight:500}
.main-nav a{color:var(--ink);text-decoration:none;padding-bottom:6px}
.main-nav a.is-active{color:var(--blue);border-bottom:2px solid var(--blue)}

/* hero */
.hero{position:absolute;left:0;top:98px;width:1200px;height:623px;
  background:linear-gradient(180deg,#3d4b5c 0%,#b97a3a 35%,#e09a3c 52%,#6b5240 75%,#2b2a2a 100%)}
.hero-title{position:absolute;left:113px;top:180px;font-family:"Archivo",sans-serif;font-weight:700;font-size:56px;line-height:58px;color:var(--white)}
.hero-text{position:absolute;left:113px;top:300px;width:470px;font-family:var(--copy-font);font-size:17px;line-height:32px;color:var(--white)}
.btn-solid{position:absolute;display:flex;align-items:center;justify-content:center;border-radius:26px;background:linear-gradient(180deg,var(--blue-bright),var(--blue-deep));color:var(--white);font-weight:600;font-size:17px}
.hero-arrow{position:absolute;top:300px}
.hero-dots{position:absolute;left:563px;top:568px;display:flex;gap:8px}
.hero-dots span{width:12px;height:12px;border-radius:50%;background:rgba(255,255,255,.55)}
.hero-dots span.on{background:var(--white)}

/* section labels */
.eyebrow{position:absolute;font-family:"Archivo",sans-serif;font-weight:600;font-size:16px;color:var(--blue);letter-spacing:.3px}
.section-title{position:absolute;font-family:"Archivo",sans-serif;font-weight:600;font-size:38px;line-height:42px;color:var(--ink)}
.center{left:0;width:1200px;text-align:center}

/* about */
.about{position:absolute;left:0;top:721px;width:1200px;height:563px}
.about-ghost{position:absolute;left:0;top:38px;font-family:"Archivo",sans-serif;font-weight:800;font-size:118px;color:#eef5fc;white-space:nowrap;letter-spacing:2px}
.about-text{position:absolute;left:111px;top:200px;width:440px;font-family:var(--copy-font);font-size:13px;line-height:26.8px;color:var(--body)}
.about-frame{position:absolute;left:630px;top:108px;width:458px;height:350px;border:3px solid var(--blue-deep)}
.about-photo{position:absolute;left:617px;top:124px;width:456px;height:352px;background:linear-gradient(135deg,#8ea3b6,#c7b394 50%,#4f6a86)}

/* services */
.services{position:absolute;left:0;top:1284px;width:1200px;height:599px;background:var(--band)}
.service-card{position:absolute;top:182px;width:307px;height:319px;background:var(--white)}
.service-num{position:absolute;right:8px;top:22px;font-family:"Archivo",sans-serif;font-weight:800;font-size:110px;line-height:110px;color:#eceef1}
.service-icon{position:absolute;left:22px;top:24px}
.service-title{position:absolute;left:18px;top:108px;font-size:22px;font-weight:500;color:var(--ink)}
.service-text{position:absolute;left:18px;top:148px;width:265px;font-family:var(--copy-font);font-size:15px;line-height:24px;color:var(--body)}
.read-more{position:absolute;left:18px;top:269px;font-size:14px;font-weight:600;color:var(--blue);display:flex;align-items:center;gap:6px}

/* why */
.why{position:absolute;left:0;top:1883px;width:1200px;height:517px}
.why-photo{position:absolute;left:0;top:0;width:599px;height:517px;background:linear-gradient(160deg,#d7b04a 0%,#8c8a7e 45%,#6b8bb3 100%)}
.why-panel{position:absolute;left:599px;top:0;width:601px;height:517px;background:linear-gradient(180deg,#0f58b5 0%,#0a3d9a 60%,#07307f 100%)}
.why-title{position:absolute;left:60px;top:110px;font-family:"Archivo",sans-serif;font-weight:600;font-size:38px;color:var(--white)}
.why-text{position:absolute;left:63px;top:170px;width:462px;font-family:var(--copy-font);font-size:12.2px;line-height:27.5px;color:var(--white)}
.btn-outline{position:absolute;display:flex;align-items:center;justify-content:center;border:2px solid var(--white);border-radius:26px;color:var(--white);font-weight:600;font-size:17px}

/* projects */
.projects{position:absolute;left:0;top:2400px;width:1200px;height:832px}
.project-tile{position:absolute;width:316px;height:264px}

/* safety */
.safety{position:absolute;left:0;top:3232px;width:1200px;height:463px;background:linear-gradient(180deg,#0f5cbc 0%,#0a3f9e 55%,#082f85 100%)}
.safety-text{position:absolute;left:180px;top:175px;width:840px;text-align:center;font-family:var(--copy-font);font-size:13.5px;line-height:28.5px;color:var(--white)}

/* news */
.news{position:absolute;left:0;top:3695px;width:1200px;height:635px}
.news-card{position:absolute;top:195px;width:313px;height:353px;background:var(--band);border-radius:10px;overflow:hidden}
.news-photo{height:211px}
.news-date{position:absolute;top:232px;left:0;width:100%;text-align:center;font-family:var(--copy-font);font-size:13px;color:var(--blue)}
.news-title{position:absolute;top:254px;left:0;width:100%;text-align:center;font-size:17.5px;font-weight:500;color:var(--ink)}
.news-text{position:absolute;top:284px;left:25px;width:263px;text-align:center;font-family:var(--copy-font);font-size:13px;line-height:26px;color:var(--body)}

/* footer */
.site-footer{position:absolute;left:0;top:4330px;width:1200px;height:358px;background:var(--footer);color:var(--white)}
.foot-head{position:absolute;top:74px;font-family:"Archivo",sans-serif;font-weight:600;font-size:16px}
.foot-field{position:absolute;height:36px;background:var(--white);border:1px solid #cfd3da;font-family:var(--copy-font);font-size:11px;color:#6a6a6a;padding:10px 8px}
.foot-btn{position:absolute;left:111px;top:199px;width:330px;height:38px;background:linear-gradient(180deg,var(--blue-bright),var(--blue-deep));display:flex;align-items:center;justify-content:center;font-family:"Archivo",sans-serif;font-weight:700;font-size:16px;letter-spacing:.5px}
.foot-list{position:absolute;top:100px;list-style:none;font-family:var(--copy-font);font-size:12.5px;line-height:26.5px}
.foot-contact{position:absolute;left:861px;top:100px;font-family:var(--copy-font);font-size:12.5px;line-height:26.5px}
.foot-contact div{display:flex;align-items:center;gap:8px}
.foot-rule{position:absolute;left:111px;top:288px;width:978px;height:1px;background:#333}
.copyright{position:absolute;left:111px;top:312px;font-family:var(--copy-font);font-size:12.5px}
.social{position:absolute;left:925px;top:304px;display:flex;gap:12px}
.social span{width:32px;height:32px;border-radius:50%;background:var(--blue-bright)}
</style>
</head>
<body>

<header class="site-header">
  <div class="brand">
    <div class="brand-mark"></div>
    <div class="brand-name">DUNMORE RIDGE CONSTRUCTION</div>
  </div>
  <div class="contact-bar">
    <div class="contact-item">
      <span class="contact-icon"><svg width="16" height="16" viewBox="0 0 24 24"><path fill="#fff" d="M6.6 10.8a15.1 15.1 0 0 0 6.6 6.6l2.2-2.2c.3-.3.7-.4 1-.2 1.1.4 2.3.6 3.6.6.6 0 1 .4 1 1V20c0 .6-.4 1-1 1A17 17 0 0 1 3 4c0-.6.4-1 1-1h3.5c.6 0 1 .4 1 1 0 1.3.2 2.5.6 3.6.1.3 0 .7-.2 1z"/></svg></span>
      555-014-2270
    </div>
    <div class="contact-item">
      <span class="contact-icon"><svg width="16" height="16" viewBox="0 0 24 24"><path fill="none" stroke="#fff" stroke-width="2" d="M3 6h18v12H3z M3 6l9 7 9-7"/></svg></span>
      info@dunmoreridgebuild.com
    </div>
  </div>
  <nav class="main-nav">
    <a class="is-active">Home</a><a>About</a><a>Services</a><a>Projects</a><a>News</a><a>Contact us</a>
  </nav>
</header>

<section class="hero" role="img" aria-label="Construction crew in safety vests reviewing plans on a site at sunset with a tower crane">
  <h1 class="hero-title">DUNMORE RIDGE<br>CONSTRUCTION</h1>
  <p class="hero-text">Sed ut perspiciatis unde omnis iste naerror sit voluptatem accusantium doloremque laudantium</p>
  <div class="btn-solid" style="left:113px;top:390px;width:173px;height:46px">Get Started</div>
  <svg class="hero-arrow" style="left:74px" width="16" height="28" viewBox="0 0 16 28"><path d="M14 2 2 14l12 12" fill="none" stroke="#fff" stroke-width="1.5" opacity=".8"/></svg>
  <svg class="hero-arrow" style="left:1110px" width="16" height="28" viewBox="0 0 16 28"><path d="M2 2l12 12L2 26" fill="none" stroke="#fff" stroke-width="1.5" opacity=".8"/></svg>
  <div class="hero-dots"><span></span><span class="on"></span><span></span><span></span></div>
</section>

<section class="about">
  <div class="about-ghost">WHO WE ARE</div>
  <div class="eyebrow" style="left:111px;top:118px">ABOUT US</div>
  <h2 class="section-title" style="left:111px;top:143px">WHO WE ARE</h2>
  <p class="about-text">Lorem ipsum dolor sit amet, consectetur adipiscing elit, sed do eiusmod tempor incididunt ut labore et dolore magna aliqua. Qusum suspendisse ultrices gravida. Risus commodo viverra maecenas accumsan lacus vel facilisis. Lorem ipsum dolor sit amet, consectetur adipcing elit, eiusmod tempor incididunt ut labore et dolore magna alua. Quipsum suspendisse ultrices gravida. Risus commodo viverra maecenas accumsan lacus vel facilisis.</p>
  <div class="btn-solid" style="left:111px;top:412px;width:175px;height:51px">Learn More</div>
  <div class="about-frame"></div>
  <div class="about-photo" role="img" aria-label="Site workers in hard hats shaking hands with a client inside a steel-framed building"></div>
</section>

<section class="services">
  <div class="eyebrow center" style="top:88px">OUR SERVICES</div>
  <h2 class="section-title center" style="top:112px">WHAT WE OFFER</h2>

  <article class="service-card" style="left:111px">
    <div class="service-num">01</div>
    <svg class="service-icon" width="78" height="72" viewBox="0 0 78 72" fill="none" stroke="#0b3a94" stroke-width="2.5"><path d="M14 70V10h34v60M48 30h16v40M4 70h70M22 18h6M34 18h6M22 28h6M34 28h6M22 38h6M34 38h6M22 48h6M34 48h6M26 70V58h10v12M54 40h4M54 50h4M54 60h4"/></svg>
    <h3 class="service-title">Lorem Ipsum</h3>
    <p class="service-text">Sed ut perspiciatis unde omnis iste natus error sit volupm accusantium doloremque laudantium, totam rem aperiam, eaque ipsa</p>
    <div class="read-more">Read More <svg width="14" height="10" viewBox="0 0 14 10"><path d="M0 5h12M8 1l4 4-4 4" fill="none" stroke="#0b3a94" stroke-width="1.5"/></svg></div>
  </article>

  <article class="service-card" style="left:444px">
    <div class="service-num">02</div>
    <svg class="service-icon" width="80" height="60" viewBox="0 0 80 60" fill="none" stroke="#0b3a94" stroke-width="2.5"><path d="M8 4h26v18H8zM4 22h44v14H4zM48 30l14-6 14 18H58M6 36h44a8 8 0 0 1 0 16H6a8 8 0 0 1 0-16z"/><circle cx="10" cy="44" r="3"/><circle cx="22" cy="44" r="3"/><circle cx="34" cy="44" r="3"/><circle cx="46" cy="44" r="3"/></svg>
    <h3 class="service-title">Lorem Ipsum</h3>
    <p class="service-text">Sed ut perspiciatis unde omnis iste natus error sit volupm accusantium doloremque laudantium, totam rem aperiam, eaque ipsa</p>
    <div class="read-more">Read More <svg width="14" height="10" viewBox="0 0 14 10"><path d="M0 5h12M8 1l4 4-4 4" fill="none" stroke="#0b3a94" stroke-width="1.5"/></svg></div>
  </article>

  <article class="service-card" style="left:778px">
    <div class="service-num">03</div>
    <svg class="service-icon" width="70" height="70" viewBox="0 0 70 70" fill="none" stroke="#0b3a94" stroke-width="2.5"><path d="M38 68V8M44 68V8M30 8h36M38 8l8-6 20 6M58 8v18M54 26h8v8h-8zM4 68V30h20v38M2 68h66M10 38h8M10 46h8M10 54h8"/></svg>
    <h3 class="service-title">Lorem Ipsum</h3>
    <p class="service-text">Sed ut perspiciatis unde omnis iste natus error sit volupm accusantium doloremque laudantium, totam rem aperiam, eaque ipsa</p>
    <div class="read-more">Read More <svg width="14" height="10" viewBox="0 0 14 10"><path d="M0 5h12M8 1l4 4-4 4" fill="none" stroke="#0b3a94" stroke-width="1.5"/></svg></div>
  </article>
</section>

<section class="why">
  <div class="why-photo" role="img" aria-label="Two site engineers with a hard hat and plans standing in front of a yellow excavator"></div>
  <div class="why-panel">
    <h2 class="why-title">WHY CHOOSE US</h2>
    <p class="why-text">Sed ut perspiciatis unde omnis iste natus error sit voluptatem accusantium doloremque laudantium, totam rem aperiam, eaque ipsa quae ab illo inventore veritatis et quasi architecto beatae vitae dicta sunt explicabo. Nemo enim ipsam voluptatem quia voluptas sit aspernur aut odit aut fugit, sed quia consequuntur magni dolores eos qui ratione voluptate sequi nesciunt. Neque porro quisquam est, qui dolorem ipsum quia dolor sit amet, consectetur, adipisci velit, sed quia non numquam eius modi tempora incidunt</p>
    <div class="btn-outline" style="left:62px;top:382px;width:173px;height:48px">Learn More</div>
  </div>
</section>

<section class="projects">
  <div class="eyebrow center" style="top:82px">OUR WORKS</div>
  <h2 class="section-title center" style="top:106px">LATEST PROJECTS</h2>
  <div class="project-tile" style="left:111px;top:180px;background:linear-gradient(180deg,#2c6fd1,#3a4d66 60%,#6d6b52)" role="img" aria-label="Completed mid-rise commercial building with glass facade"></div>
  <div class="project-tile" style="left:442px;top:180px;background:linear-gradient(180deg,#1f63cf,#1c4c9c 60%,#4a6074)" role="img" aria-label="Glass commercial building beside a reflecting pool"></div>
  <div class="project-tile" style="left:774px;top:180px;background:linear-gradient(180deg,#0f1f3a,#4a3b28 55%,#1c1c1c)" role="img" aria-label="Lit multi-storey building at dusk"></div>
  <div class="project-tile" style="left:111px;top:459px;background:linear-gradient(180deg,#c7d2dc,#8e938c 55%,#5d6a4c)" role="img" aria-label="Aerial view of a large office complex"></div>
  <div class="project-tile" style="left:442px;top:459px;background:linear-gradient(180deg,#d9e6f4,#4a84c8 50%,#5f7b58)" role="img" aria-label="Blue glass tower with landscaped forecourt"></div>
  <div class="project-tile" style="left:774px;top:459px;background:linear-gradient(180deg,#2a3550,#7a5a38 55%,#2c2520)" role="img" aria-label="Modern commercial building lit at twilight"></div>
</section>

<section class="safety">
  <h2 class="section-title center" style="top:118px;color:var(--white)">SAFETY AND QUALITY</h2>
  <p class="safety-text">Lorem ipsum dolor sit amet, consectetur adipiscing elit, sed do eiusmod tempor incididunt ut labore et dolore magna aliqua. Ut enim ad minim veniam, quis nostrud exercitation ullamco laboris nisi ut aliquip ex ea commodo consequat. Duis aute irure dolor in reprehenderit in voluptate velit esse cillum dolore eu fugiat nulla</p>
  <div class="btn-outline" style="left:502px;top:290px;width:196px;height:50px">Learn More</div>
</section>

<section class="news">
  <div class="eyebrow center" style="top:83px">UPDATES</div>
  <h2 class="section-title center" style="top:107px">LATEST NEWS</h2>

  <article class="news-card" style="left:111px">
    <div class="news-photo" style="background:linear-gradient(135deg,#c9c2b4,#d88a3c 40%,#2b4f86 75%,#3a3a3a)" role="img" aria-label="Overhead view of workers in hard hats reviewing drawings at a table"></div>
    <div class="news-date">11 AUG 2021</div>
    <h3 class="news-title">The standard Lorem Ipsum pas</h3>
    <p class="news-text">Lorem ipsum dolor sit amet, consectetur adipiscing elit, sed do eiusmod</p>
  </article>
  <article class="news-card" style="left:444px">
    <div class="news-photo" style="background:linear-gradient(180deg,#a9b4c0,#6f7884 55%,#3a3f46)" role="img" aria-label="Worker in a safety vest walking on an elevated steel deck"></div>
    <div class="news-date">11 AUG 2021</div>
    <h3 class="news-title">The standard Lorem Ipsum pas</h3>
    <p class="news-text">Lorem ipsum dolor sit amet, consectetur adipiscing elit, sed do eiusmod</p>
  </article>
  <article class="news-card" style="left:776px">
    <div class="news-photo" style="background:linear-gradient(160deg,#2a4d8f,#5e7fb0 45%,#e0a15a 80%,#22304a)" role="img" aria-label="Steel building frame and crane silhouetted against a sunset"></div>
    <div class="news-date">11 AUG 2021</div>
    <h3 class="news-title">The standard Lorem Ipsum pas</h3>
    <p class="news-text">Lorem ipsum dolor sit amet, consectetur adipiscing elit, sed do eiusmod</p>
  </article>
</section>

<footer class="site-footer">
  <div class="foot-head" style="left:111px">GET INSIGHTS &amp; UPDATES</div>
  <div class="foot-field" style="left:111px;top:108px;width:160px">Name</div>
  <div class="foot-field" style="left:279px;top:108px;width:162px">Name</div>
  <div class="foot-field" style="left:111px;top:154px;width:330px">Enter Email</div>
  <div class="foot-btn">SUBSCRIBE</div>

  <div class="foot-head" style="left:508px">QUCIK LINKS</div>
  <ul class="foot-list" style="left:508px">
    <li>- Home</li><li>- Who We Are</li><li>- Services</li><li>- Projects</li><li>- News</li><li>- Contact us</li>
  </ul>

  <div class="foot-head" style="left:674px">OTHER LINKS</div>
  <ul class="foot-list" style="left:674px">
    <li>- Code Of Conduct</li><li>- Privacy</li><li>- Cookies Policy</li><li>- Terms &amp; Conditions</li><li>- Sitemap</li>
  </ul>

  <div class="foot-head" style="left:861px">CONTACT INFO</div>
  <div class="foot-contact">
    <div><svg width="10" height="13" viewBox="0 0 10 13"><path fill="#fff" d="M5 0a5 5 0 0 0-5 5c0 3.5 5 8 5 8s5-4.5 5-8a5 5 0 0 0-5-5zm0 7a2 2 0 1 1 0-4 2 2 0 0 1 0 4z"/></svg>123 Your Adress Goes Here.</div>
    <div style="padding-left:18px">CA, 1234567</div>
    <div><svg width="12" height="12" viewBox="0 0 24 24"><path fill="#fff" d="M6.6 10.8a15.1 15.1 0 0 0 6.6 6.6l2.2-2.2c.3-.3.7-.4 1-.2 1.1.4 2.3.6 3.6.6.6 0 1 .4 1 1V20c0 .6-.4 1-1 1A17 17 0 0 1 3 4c0-.6.4-1 1-1h3.5c.6 0 1 .4 1 1 0 1.3.2 2.5.6 3.6.1.3 0 .7-.2 1z"/></svg>555-014-2270</div>
    <div><svg width="12" height="10" viewBox="0 0 12 10"><path fill="#fff" d="M0 0h12v10H0z"/><path d="M0 0l6 5 6-5" fill="none" stroke="#141414" stroke-width="1.2"/></svg>info@dunmoreridgebuild.com</div>
  </div>

  <div class="foot-rule"></div>
  <div class="copyright">© 2022 Dunmore Ridge Construction. All Rights Reserved.</div>
  <div class="social"><span></span><span></span><span></span><span></span></div>
</footer>

</body>
</html>
```